Dorvelan Swimming & Athletics Center

We need Business Card for a Athletics center
The logo frome the Uploaded Files ( b card fimal)
Οn one side of card we need the logo of company the Contact and the website:
1. Address:(Limassol, Cyprus 12-14 Stavrinelou str,Ano Trimeni,P.C. 4832)

2.Phone number: (+357) 25-704263

3. Mail: info@dorvelanfit.example

3. Website: www.dorvelanfit.example

Οn the other side of the card we need to write the sport of the company:

1. Artistic Gymnastics
2. Swimming
3. Gym - Fitness
4. Programs
5. Dancing
5.Tennis

From the Uploaded Files you can get the logo.In a logo is behind the black color which can be removed from logo.

Υou can use that color you want.
.
Updates

Industry/Entity Type

Business

Font styles to use
Decorative

Colors
0555a3
ffcf3e
3176b5
0692cd
add136
f04a50
000000
cfcfcf
9d9d9d

Requirements
Should not have
• photos with faces
• photo fro the Website:www.dorvelanfit.example

```html
<!DOCTYPE html>
<html lang="en">
<head>
<meta charset="utf-8">
<title>Dorvelan Swimming &amp; Athletics Center – Business Card</title>
<link rel="stylesheet" href="https://fonts.googleapis.com/css2?family=Lato:wght@300;400;700;900&display=swap">
<style>
  :root {
    --ink: #0b0b0b;
    --band: #161616;
    --yellow: #ffcf3e;
    --yellow-deep: #f2bb2a;
    --slogan-ink: #1a1a1a;
    --backdrop: #e4e6e8;
  }
  * { margin: 0; padding: 0; box-sizing: border-box; }
  html, body {
    width: 1200px; height: 1200px; overflow: hidden;
    background: var(--backdrop);
    font-family: "Lato", Arial, sans-serif;
  }
  .canvas { position: relative; width: 1200px; height: 1200px; }
  .card { position: absolute; left: 248px; width: 704px; height: 402px; display: block; }
  .card--front { top: 106px; }
  .card--back { top: 625px; }
  .fill-ink { fill: var(--ink); }
  .fill-band { fill: var(--band); }
  .fill-yellow { fill: var(--yellow); }
  .fill-yellow-deep { fill: var(--yellow-deep); }
  .brand-name { fill: var(--yellow); font-family: "Lato", Arial, sans-serif; font-weight: 900; font-size: 54px; letter-spacing: 2px; }
  .brand-mark { fill: none; stroke: var(--yellow); stroke-width: 4; }
  .holder-name { fill: var(--yellow); font-weight: 400; font-size: 32px; }
  .holder-role { fill: var(--yellow); font-weight: 400; font-size: 25px; }
  .slogan { fill: var(--slogan-ink); font-weight: 400; font-size: 27px; }
  .contact { fill: var(--yellow); font-weight: 300; font-size: 20px; }
  .contact--phone { letter-spacing: 3px; }
  .icon { fill: var(--yellow); }
  .icon-line { fill: none; stroke: var(--yellow); stroke-width: 2.4; stroke-linecap: round; }
  .emblem-ring { fill: none; stroke: var(--yellow); stroke-width: 6; }
  .emblem-name { fill: var(--yellow); font-weight: 900; font-size: 30px; letter-spacing: 1px; }
  .sport { fill: var(--yellow); font-weight: 300; font-size: 21px; }
</style>
</head>
<body>
<main class="canvas">

  <!-- Front: brand, holder and contact details -->
  <svg class="card card--front" viewBox="0 0 880 503" aria-label="Business card front">
    <rect class="fill-ink" width="880" height="503"/>
    <polygon class="fill-yellow" points="730,0 880,0 880,503 0,503 0,468 635,468 675,268 705,148 705,60 718,60"/>
    <rect class="fill-band" y="60" width="880" height="88"/>
    <polygon class="fill-yellow-deep" points="345,185 880,185 880,268 282,268"/>

    <text class="brand-name" x="52" y="125">DORVELAN</text>
    <circle class="brand-mark" cx="430" cy="105" r="34"/>

    <text class="holder-name" x="820" y="106" text-anchor="end">YOUR FULL NAME</text>
    <text class="holder-role" x="820" y="132" text-anchor="end">Designation</text>

    <text class="slogan" x="820" y="235" text-anchor="end">YOUR AMAZING SLOGAN GOES HERE</text>

    <g class="contact-list">
      <path class="icon" d="M60 297a8 8 0 0 1 8 8c0 6-8 15-8 15s-8-9-8-15a8 8 0 0 1 8-8zm0 5a3 3 0 1 0 0 6a3 3 0 0 0 0-6z"/>
      <text class="contact" x="88" y="315">Limassol, Cyprus 12-14 Stavrinelou str,</text>
      <text class="contact" x="88" y="340">Ano Trimeni,P.C. 4832)</text>

      <path class="icon" d="M54 356c2-2 4-2 5 0l3 4c1 2 0 3-1 4l-1 1c1 3 4 6 7 7l1-1c1-1 2-2 4-1l4 3c2 1 2 3 0 5l-2 2c-3 2-9 0-15-6s-8-12-6-15z"/>
      <text class="contact contact--phone" x="88" y="373">+357  25-704263</text>

      <rect class="icon" x="52" y="395" width="19" height="13" rx="1"/>
      <path d="M53 396l8.5 7l8.5-7" fill="none" stroke="var(--ink)" stroke-width="1.6"/>
      <text class="contact" x="90" y="407">info@dorvelanfit.example</text>

      <circle class="icon" cx="55" cy="439" r="2.4"/>
      <path class="icon-line" d="M53 431a9 9 0 0 1 9 9M53 425a15 15 0 0 1 15 15M53 419a21 21 0 0 1 21 21"/>
      <text class="contact" x="90" y="442">www.dorvelanfit.example</text>
    </g>
  </svg>

  <!-- Back: emblem and list of sports -->
  <svg class="card card--back" viewBox="0 0 877 501" aria-label="Business card back">
    <rect class="fill-yellow" width="877" height="501"/>
    <rect class="fill-ink" y="43" width="877" height="422"/>

    <circle class="emblem-ring" cx="431" cy="224" r="112"/>
    <text class="emblem-name" x="431" y="235" text-anchor="middle">DORVELAN</text>

    <g class="sport-list">
      <polygon class="icon" points="58,399 66,404 58,409"/>
      <text class="sport" x="78" y="412">ARTISTIC GYMNASTICS</text>
      <polygon class="icon" points="58,429 66,434 58,439"/>
      <text class="sport" x="78" y="442">SWIMMING</text>

      <polygon class="icon" points="369,399 377,404 369,409"/>
      <text class="sport" x="388" y="412">GYM - FITNESS</text>
      <polygon class="icon" points="369,429 377,434 369,439"/>
      <text class="sport" x="389" y="442">PROGRAMS</text>

      <polygon class="icon" points="621,399 629,404 621,409"/>
      <text class="sport" x="641" y="412">DANCING</text>
      <polygon class="icon" points="621,429 629,434 621,439"/>
      <text class="sport" x="642" y="442">TENNIS</text>
    </g>
  </svg>

</main>
</body>
</html>
```